Leap Forward Flyer

Marketing Promo Flyer

***I uploaded the 2022 version just as an example. I'm open to NEW designs!

Brightmoor 50th Anniversary Logo
FULL STEAM
New customers receive up to $3,000 toward your orders!

LEAP FORWARD
Buy $10,000 Receive $500
Buy $25,000 Receive $500
Buy $50,000 Receive $500
Buy $200,000 Receive $500

KEEP ROLLING
Complete all levels of Leap Forward then the following year spend the same or more as previous year and get $1,000!

Terms and conditions: A new customer is a contactor that has purchased less than $2,000 with Brightmoor Supply in the past six (6) months from the time of the first eligible voucher. Materials must be paid. The customer has 12 months from the date of the first qualifying purchase to reach all levels of Leap forward. If you reach all four levels of Leap Forward, you are then eligible for Keep Rolling. Keep Rolling voucher may be rewarded when you match or beat the previous year purchase. The vouchers are to be used toward future purchases but may not be used to pay off previous balance on the customer's account. No one-time purchasers. This promotion and your participation in it is void where prohibited by law, rules or regulations. Brightmoor Supply reserves the right to cancel, suspend, and/or modify this promotion at any time, for any reason, without prior notice. Vouchers are valid up to one year after issued date. Promotion expires December 31, 2023. All rights reserved by Brightmoor Supply.

```html
<!DOCTYPE html>
<html lang="en">
<head>
<meta charset="utf-8">
<title>Leap Forward Flyer</title>
<link rel="stylesheet" href="https://fonts.googleapis.com/css2?family=Montserrat:wght@300;400;500;600;700;800&display=swap">
<style>
  :root {
    --navy: #2b3285;
    --royal: #2a56a8;
    --sky: #2d86c9;
    --orange: #f0a21f;
    --orange-light: #f6c548;
    --panel: #f3f3f3;
    --swoosh: #cdcdcd;
    --ink: #111111;
    --white: #ffffff;
    --black: #0c0c0c;
  }
  * { box-sizing: border-box; margin: 0; padding: 0; }
  html, body { width: 945px; height: 1200px; overflow: hidden; background: var(--white); }
  body { font-family: "Montserrat", Arial, sans-serif; color: var(--ink); }
  .flyer { position: relative; width: 945px; height: 1200px; overflow: hidden; background: var(--white); }

  .swoosh { position: absolute; left: 0; top: 150px; width: 945px; height: 70px; }
  .offer-panel { position: absolute; left: 0; top: 213px; width: 945px; height: 250px; background: var(--panel); }

  .brand-mark { position: absolute; left: 600px; top: 92px; display: flex; align-items: center; gap: 10px; }
  .brand-mark .dot { width: 22px; height: 22px; border-radius: 50%; background: var(--navy); }
  .brand-mark .name { font-size: 22px; font-weight: 700; color: var(--navy); letter-spacing: .3px; }

  .photo-boat {
    position: absolute; left: -30px; top: 57px; width: 484px; height: 484px; border-radius: 50%;
    border: 5px solid var(--white);
    background: linear-gradient(180deg, #f2f2f2 0%, #d6d6d6 45%, #e89a6a 52%, #35b5d8 58%, #1684b8 80%, #0d6fa6 100%);
    z-index: 3;
  }

  .headline-main { position: absolute; left: 481px; top: 240px; font-size: 53px; letter-spacing: -2px; color: var(--navy); line-height: 1; z-index: 2; }
  .headline-main .light { font-weight: 300; }
  .headline-main .bold { font-weight: 800; }

  .ribbon { position: absolute; left: 449px; top: 315px; width: 486px; height: 45px; z-index: 2; }
  .ribbon-text { position: absolute; left: 480px; top: 322px; font-size: 25px; font-weight: 500; color: var(--ink); z-index: 3; }

  .amount { position: absolute; left: 467px; top: 382px; font-size: 76px; font-weight: 700; color: var(--navy); letter-spacing: -3px; line-height: 1; z-index: 2; }
  .amount-note { position: absolute; left: 719px; top: 390px; font-size: 32px; font-weight: 400; line-height: .95; letter-spacing: -1px; color: var(--ink); z-index: 2; }

  .tiers-band { position: absolute; left: 0; top: 462px; width: 945px; height: 343px; background: linear-gradient(90deg, #2b7cc4 0%, #2a65b6 60%, #2a4fa2 100%); }

  .photo-leap {
    position: absolute; left: 30px; top: 518px; width: 308px; height: 308px; border-radius: 50%;
    background: linear-gradient(160deg, #79b7e6 0%, #5aa3dc 55%, #3f4a5e 100%);
    border: 4px solid var(--white); box-shadow: -4px 4px 0 0 var(--navy);
    z-index: 2;
  }

  .tiers-title-top { position: absolute; left: 424px; top: 498px; font-size: 47px; font-weight: 300; color: var(--white); letter-spacing: -1px; line-height: 1; z-index: 3; }
  .tiers-title-bar { position: absolute; left: 321px; top: 545px; width: 370px; height: 57px; z-index: 1; }
  .tiers-title-bottom { position: absolute; left: 424px; top: 551px; font-size: 45px; font-weight: 700; color: var(--sky); letter-spacing: -2px; line-height: 1; z-index: 3; }

  .tier-list { position: absolute; left: 416px; top: 626px; list-style: none; z-index: 3; }
  .tier-list li { display: flex; align-items: center; height: 38.5px; font-size: 28px; color: var(--white); letter-spacing: -1px; white-space: nowrap; }
  .tier-list .tick { width: 31px; height: 31px; margin-right: 14px; flex: none; }
  .tier-list .buy { font-weight: 700; margin-right: 7px; }
  .tier-list .spend { font-weight: 300; margin-right: 7px; }
  .tier-list .reward { font-weight: 700; color: var(--orange-light); }

  .loyalty-area { position: absolute; left: 0; top: 805px; width: 945px; height: 231px; background: var(--white); }
  .photo-beach {
    position: absolute; left: 620px; top: 805px; width: 325px; height: 175px;
    background: linear-gradient(90deg, rgba(255,255,255,1) 0%, #cfeaf3 25%, #6b8f4f 55%, #4a6b32 75%, #86a866 100%);
  }
  .photo-water {
    position: absolute; left: 0; top: 968px; width: 945px; height: 68px;
    background: linear-gradient(180deg, #dff3fa 0%, #6cc6e8 35%, #2a9fd6 70%, #1b86c3 100%);
  }
  .loyalty-title { position: absolute; left: 34px; top: 850px; font-size: 54px; letter-spacing: -2px; line-height: 1; z-index: 2; }
  .loyalty-title .light { font-weight: 300; color: var(--ink); }
  .loyalty-title .bold { font-weight: 700; color: var(--sky); }
  .loyalty-copy { position: absolute; left: 36px; top: 919px; width: 620px; font-size: 19px; font-weight: 400; line-height: 25px; color: var(--ink); z-index: 2; }
  .loyalty-copy strong { font-weight: 800; }

  .terms { position: absolute; left: 0; top: 1036px; width: 945px; height: 120px; background: linear-gradient(180deg, #000 0%, #1b1b1b 100%); padding: 9px 36px 0 36px; }
  .terms p { font-size: 11px; font-weight: 400; line-height: 13.5px; color: #e8e8e8; text-align: justify; }
  .terms strong { font-size: 13px; font-weight: 700; color: var(--white); }
  .expiry { position: absolute; left: 0; top: 1156px; width: 945px; height: 20px; background: var(--white); text-align: center; font-size: 11px; font-weight: 700; line-height: 20px; color: var(--ink); }
  .footer-bar { position: absolute; left: 0; top: 1176px; width: 945px; height: 24px; background: linear-gradient(180deg, #2a2a2a, #050505); }
</style>
</head>
<body>
<main class="flyer">

  <svg class="swoosh" viewBox="0 0 945 70" preserveAspectRatio="none" aria-hidden="true">
    <path d="M450 70 C 520 10, 700 45, 945 45 L945 70 Z" fill="var(--swoosh)"/>
    <path d="M450 70 C 540 30, 700 55, 945 50 L945 70 Z" fill="#e4e4e4"/>
  </svg>

  <div class="brand-mark">
    <span class="dot"></span>
    <span class="name">Brightmoor Supply</span>
  </div>

  <section class="offer-panel"></section>
  <div class="photo-boat" role="img" aria-label="Paper boat folded from a banknote floating on clear blue water"></div>

  <h1 class="headline-main"><span class="light">FULL </span><span class="bold">STEAM</span></h1>

  <svg class="ribbon" viewBox="0 0 486 45" preserveAspectRatio="none" aria-hidden="true">
    <defs>
      <linearGradient id="ribbonFill" x1="0" y1="0" x2="1" y2="0">
        <stop offset="0" stop-color="var(--orange)"/>
        <stop offset="0.5" stop-color="var(--orange-light)"/>
        <stop offset="1" stop-color="var(--orange)"/>
      </linearGradient>
    </defs>
    <polygon points="6,0 452,0 486,45 0,45" fill="url(#ribbonFill)"/>
  </svg>
  <p class="ribbon-text">New customers receive up to</p>

  <p class="amount">$3,000</p>
  <p class="amount-note">toward your<br>orders!</p>

  <section class="tiers-band"></section>
  <div class="photo-leap" role="img" aria-label="Person in a dark jacket leaping across a blue sky"></div>

  <svg class="tiers-title-bar" viewBox="0 0 370 57" preserveAspectRatio="none" aria-hidden="true">
    <defs>
      <linearGradient id="barFill" x1="0" y1="0" x2="1" y2="0">
        <stop offset="0" stop-color="#ffffff" stop-opacity="0"/>
        <stop offset="0.3" stop-color="#ffffff"/>
        <stop offset="1" stop-color="#f1f1f1"/>
      </linearGradient>
    </defs>
    <polygon points="0,0 335,0 370,57 0,57" fill="url(#barFill)"/>
  </svg>
  <h2 class="tiers-title-top">LEAP</h2>
  <h2 class="tiers-title-bottom">FORWARD</h2>

  <ul class="tier-list">
    <li><svg class="tick" viewBox="0 0 32 32" aria-hidden="true"><circle cx="16" cy="16" r="15" fill="var(--orange)"/><path d="M10 16.5 L14.5 21 L22.5 12" fill="none" stroke="var(--royal)" stroke-width="3" stroke-linecap="round" stroke-linejoin="round"/></svg><span class="buy">Buy</span><span class="spend">$10,000 Receive</span><span class="reward">$500</span></li>
    <li><svg class="tick" viewBox="0 0 32 32" aria-hidden="true"><circle cx="16" cy="16" r="15" fill="var(--orange)"/><path d="M10 16.5 L14.5 21 L22.5 12" fill="none" stroke="var(--royal)" stroke-width="3" stroke-linecap="round" stroke-linejoin="round"/></svg><span class="buy">Buy</span><span class="spend">$25,000 Receive</span><span class="reward">$500</span></li>
    <li><svg class="tick" viewBox="0 0 32 32" aria-hidden="true"><circle cx="16" cy="16" r="15" fill="var(--orange)"/><path d="M10 16.5 L14.5 21 L22.5 12" fill="none" stroke="var(--royal)" stroke-width="3" stroke-linecap="round" stroke-linejoin="round"/></svg><span class="buy">Buy</span><span class="spend">$50,000 Receive</span><span class="reward">$500</span></li>
    <li><svg class="tick" viewBox="0 0 32 32" aria-hidden="true"><circle cx="16" cy="16" r="15" fill="var(--orange)"/><path d="M10 16.5 L14.5 21 L22.5 12" fill="none" stroke="var(--royal)" stroke-width="3" stroke-linecap="round" stroke-linejoin="round"/></svg><span class="buy">Buy</span><span class="spend">$200,000 Receive</span><span class="reward">$500</span></li>
  </ul>

  <section class="loyalty-area"></section>
  <div class="photo-beach" role="img" aria-label="Tropical island shore lined with palm trees"></div>
  <div class="photo-water" role="img" aria-label="Band of turquoise ocean water with foam"></div>
  <h2 class="loyalty-title"><span class="light">KEEP </span><span class="bold">ROLLING</span></h2>
  <p class="loyalty-copy">Complete all levels of Leap Forward then the following year spend the same or more as previous year and get <strong>$1,000!</strong></p>

  <footer class="terms">
    <p><strong>Terms and conditions:</strong> A new customer is a contactor that has purchased less than $2,000 with Brightmoor Supply in the past six (6) months from the time of the first eligible voucher. Materials must be paid. The customer has 12 months from the date of the first qualifying purchase to reach all levels of Leap forward. If you reach all four levels of Leap Forward, you are then eligible for Keep Rolling. Keep Rolling voucher may be rewarded when you match or beat the previous year purchase. The vouchers are to be used toward future purchases but may not be used to pay off previous balance on the customer's account. No one-time purchasers. This promotion and your participation in it is void where prohibited by law, rules or regulations. Brightmoor Supply reserves the right to cancel, suspend, and/or modify this promotion at any time, for any reason, without prior notice. Vouchers are valid up to one year after issued date.</p>
  </footer>
  <p class="expiry">Promotion expires December 31, 2023. All rights reserved by Brightmoor Supply.</p>
  <div class="footer-bar"></div>

</main>
</body>
</html>
```